Buchcover-Design für Drama/Thriller/Krimi
Zielgruppe
Wir sind eine Publikation und suchen aktuell eine Design für ein Cover eines Drama-Thriller-Krimi Buches.
Zielgruppe sind alle Menschen ab 18 Jahren.
Aufgabenstellung
Es sollte zu einem Drama-Thriller-Krimi passen. Das Buch beinhaltet knapp 280 Seiten und es endet mit einem Selbstmord am Strand.
Das Buch wird heißen: kuşlar yağmurda. Es ist türkisch und heißt 'die Vögel sind im kalten Regen'.
Es handelt über folgendes: Ein Kind wird entführt - es wird die Organ Mafia beschuldigt am Ende stellt sich heraus das der neue Partner der Mutter das Kind entführt hat. Die Mutter wusste Bescheid. Die Geschichte wird von der Sicht eines Journalisten erzählt. Der Mann der Selbstmord begeht ist der Journalist.
Der Autor ist Kemal Duruöz und soll auch auf dem Cover sein. Hinten auf der Rückseite soll ein Platz für einen Kurztext gelassen werden.
Buchformat ist : 13,5×19,5 cm Hochformat.
Das Design des Covers soll die Trauer wiedergeben.
Tipp: Zb. könnte es ein Mann am Strand alleine widerspiegeln. Wir sind aber offen auch für andere Vorschläge.

```html
<!DOCTYPE html>
<html lang="tr">
<head>
<meta charset="utf-8">
<title>kuşlar yağmurda – Kemal Duruöz</title>
<link rel="stylesheet" href="https://fonts.googleapis.com/css2?family=Special+Elite&family=Raleway:wght@500&display=swap">
<style>
  :root {
    --ink-navy: #25304f;
    --cream: #f3ecdc;
    --blurb-white: #f6f7fb;
    --label-black: #0b0b0b;
    --label-text: #ffffff;
    --sky-top: #dfe6e8;
    --sky-light: #fbf4dc;
    --sky-yellow: #f8d77a;
    --sky-orange: #ef9a3a;
    --horizon-red: #c9582a;
    --sea-gold: #e8b56a;
    --sand-light: #a9562c;
    --sand-dark: #3a1a10;
  }
  * { margin: 0; padding: 0; box-sizing: border-box; }
  html, body { width: 1200px; height: 879px; overflow: hidden; background: #000; }
  .cover-wrap {
    position: relative;
    width: 1200px;
    height: 879px;
    overflow: hidden;
  }
  .beach-photo {
    position: absolute;
    inset: 0;
    background:
      radial-gradient(ellipse 90px 60px at 905px 365px, rgba(255,255,240,0.95), rgba(255,240,190,0) 100%),
      linear-gradient(180deg,
        var(--sky-top) 0%,
        var(--sky-light) 22%,
        var(--sky-yellow) 40%,
        var(--sky-orange) 48%,
        var(--horizon-red) 52.5%,
        var(--sea-gold) 54%,
        #d9a66a 60%,
        #f0b863 63.5%,
        var(--sand-light) 64.5%,
        #6b2f18 78%,
        var(--sand-dark) 100%);
  }
  .title {
    position: absolute;
    left: 622px;
    width: 578px;
    text-align: center;
    font-family: "Special Elite", "Courier New", monospace;
    color: var(--ink-navy);
    text-transform: lowercase;
    line-height: 1;
  }
  .title-line-1 { top: 36px; font-size: 140px; letter-spacing: 4px; }
  .title-line-2 { top: 178px; font-size: 100px; letter-spacing: 2px; }
  .spine {
    position: absolute;
    left: 564px;
    top: 0;
    width: 58px;
    height: 879px;
  }
  .spine-title, .spine-author {
    position: absolute;
    left: 50%;
    white-space: nowrap;
    font-family: "Special Elite", "Courier New", monospace;
    transform-origin: 0 0;
    transform: rotate(90deg);
  }
  .spine-title {
    top: 72px;
    margin-left: 20px;
    font-size: 38px;
    color: var(--ink-navy);
  }
  .spine-author {
    top: 630px;
    margin-left: 12px;
    font-size: 22px;
    color: var(--cream);
    text-transform: uppercase;
  }
  .author {
    position: absolute;
    left: 622px;
    width: 578px;
    top: 760px;
    text-align: center;
    font-family: "Special Elite", "Courier New", monospace;
    font-size: 40px;
    letter-spacing: 1px;
    color: var(--cream);
    text-transform: uppercase;
  }
  .genre-label {
    position: absolute;
    left: 846px;
    top: 817px;
    width: 132px;
    height: 62px;
    background: var(--label-black);
    color: var(--label-text);
    font-family: "Raleway", Arial, sans-serif;
    font-weight: 500;
    font-size: 25px;
    display: flex;
    align-items: center;
    justify-content: center;
  }
  .blurb-space {
    position: absolute;
    left: 339px;
    top: 718px;
    width: 203px;
    height: 124px;
    background: var(--blurb-white);
  }
</style>
</head>
<body>
  <main class="cover-wrap">
    <div class="beach-photo" role="img" aria-label="Photograph of a lonely beach at sunset: glowing orange sky, calm sea, a man in a dark jacket standing alone on the wet sand and a teddy bear lying near the waterline"></div>

    <section class="back-cover">
      <div class="blurb-space" aria-label="Space for blurb text"></div>
    </section>

    <section class="spine">
      <span class="spine-title">kuşlar yağmurda</span>
      <span class="spine-author">Kemal Duruöz</span>
    </section>

    <section class="front-cover">
      <h1>
        <span class="title title-line-1">kuşlar</span>
        <span class="title title-line-2">yağmurda</span>
      </h1>
      <p class="author">Kemal Duruöz</p>
      <p class="genre-label">ROMAN</p>
    </section>
  </main>
</body>
</html>
```